Supplement Company Needs a Protein Powder Pouch Design

We are looking for a modern and fresh design for our 500g pouches of protein powder as our current design is not eye catching or exciting enough.

This new design will be printed on both sides of a 178mm x 280mm x 101mm pouch.

We have 4 flavours. These are Banana Ice Cream, Chocolate Deluxe, Strawberries & Cream and Vanilla Ice Cream.

Industry/Entity Type

Supplement

Requirements
Must have
• Attractive and eye catching front and space for all the nutritional information and ingredients on the back.

Must clearly state 'food supplement' somewhere on the front of the pouch.
Nice to have
• Our logo is attached.
Should not have
• No health claims as these are not allowed in the UK

```html
<!DOCTYPE html>
<html lang="en">
<head>
<meta charset="utf-8">
<title>Zeal Supplements – Protein Powder Pouches</title>
<link href="https://fonts.googleapis.com/css2?family=Montserrat:wght@400;800&display=swap" rel="stylesheet">
<style>
  :root {
    --page-bg: #e6e6e6;
    --foil-light: #eeeeee;
    --foil-mid: #c9c9c9;
    --foil-dark: #a9a9a9;
    --ink: #0d0d0d;
    --type-light: #f2f2f2;
    --banana-edge: #e07f2a;
    --banana-core: #e8b22b;
    --banana-glow: #f2d83a;
    --choc-edge: #3b271c;
    --choc-core: #5b3f2e;
    --choc-glow: #b98a62;
    --wood-light: #d9b98c;
    --wood-dark: #9c7550;
  }
  * { margin: 0; padding: 0; box-sizing: border-box; }
  html, body {
    width: 1200px; height: 951px; overflow: hidden;
    background: var(--page-bg);
    font-family: "Montserrat", sans-serif;
  }
  .lineup { position: relative; width: 1200px; height: 951px; }
  .pouch {
    position: absolute; top: 110px;
    width: 531px; height: 747px;
    overflow: hidden;
  }
  .pouch--banana { left: 51px; --edge: var(--banana-edge); --core: var(--banana-core); --glow: var(--banana-glow); }
  .pouch--chocolate { left: 616px; --edge: var(--choc-edge); --core: var(--choc-core); --glow: var(--choc-glow); }

  .pouch__foil {
    position: absolute; left: 0; top: 0; width: 100%; height: 163px;
    background: linear-gradient(180deg, var(--foil-light) 0%, var(--foil-mid) 45%, var(--foil-light) 70%, var(--foil-dark) 100%);
  }
  .pouch__body {
    position: absolute; left: 0; top: 163px; width: 100%; height: 584px;
    background:
      radial-gradient(circle at 52% 45%, var(--core) 0%, var(--edge) 70%),
      var(--edge);
  }
  .pouch__handle {
    position: absolute; left: 241px; top: 0; width: 64px; height: 110px;
    background: linear-gradient(90deg, var(--wood-dark), var(--wood-light) 50%, var(--wood-dark));
  }
  .pouch__hero { position: absolute; left: 0; top: 0; width: 531px; height: 747px; }

  .brand-tab {
    position: absolute; left: 155px; top: 105px; width: 244px; height: 126px;
    background: var(--ink);
    border-radius: 3px 3px 12px 12px;
    display: flex; flex-direction: column; align-items: center; justify-content: center;
    color: var(--type-light);
  }
  .brand-tab__name { font-weight: 800; font-size: 44px; line-height: 1; letter-spacing: -1px; }
  .brand-tab__tag { font-weight: 800; font-size: 9px; letter-spacing: 6px; margin-top: 6px; padding-left: 6px; }

  .product-band {
    position: absolute; left: 20px; top: 625px; width: 491px; height: 103px;
    background: var(--ink);
    display: flex; flex-direction: column; align-items: center; justify-content: center;
    color: var(--type-light);
    font-weight: 800; font-size: 31px; line-height: 1; letter-spacing: 0.5px;
  }
  .flavour-arc { font-family: "Montserrat", sans-serif; font-weight: 400; font-size: 27px; letter-spacing: 2px; fill: var(--type-light); }
</style>
</head>
<body>
<main class="lineup">

  <article class="pouch pouch--banana">
    <div class="pouch__foil"></div>
    <div class="pouch__body"></div>
    <div class="pouch__handle" role="img" aria-label="Wooden spoon handle"></div>
    <svg class="pouch__hero" viewBox="0 0 531 747">
      <defs>
        <radialGradient id="banana-spoon" cx="50%" cy="50%" r="50%">
          <stop offset="0%" stop-color="#efe6cf"/>
          <stop offset="45%" stop-color="#c9a06d"/>
          <stop offset="80%" stop-color="#edc93a" stop-opacity="0.6"/>
          <stop offset="100%" stop-color="#f2d83a" stop-opacity="0"/>
        </radialGradient>
        <path id="banana-arc" d="M346,266 A185,185 0 0 1 251,622"/>
      </defs>
      <circle cx="283" cy="440" r="190" fill="url(#banana-spoon)" role="img" aria-label="Wooden spoon holding banana slices and a scoop of ice cream over a dotted halftone ring"/>
      <text class="flavour-arc"><textPath href="#banana-arc">BANANA ICE CREAM</textPath></text>
    </svg>
    <div class="brand-tab">
      <span class="brand-tab__name">ZEAL</span>
      <span class="brand-tab__tag">SUPPLEMENTS</span>
    </div>
    <div class="product-band"><span>PROTEIN</span><span>POWDER</span></div>
  </article>

  <article class="pouch pouch--chocolate">
    <div class="pouch__foil"></div>
    <div class="pouch__body"></div>
    <div class="pouch__handle" role="img" aria-label="Wooden spoon handle"></div>
    <svg class="pouch__hero" viewBox="0 0 531 747">
      <defs>
        <radialGradient id="choc-spoon" cx="50%" cy="50%" r="50%">
          <stop offset="0%" stop-color="#3a1f14"/>
          <stop offset="45%" stop-color="#8a6446"/>
          <stop offset="80%" stop-color="#b98a62" stop-opacity="0.5"/>
          <stop offset="100%" stop-color="#b98a62" stop-opacity="0"/>
        </radialGradient>
        <path id="choc-arc" d="M346,266 A185,185 0 0 1 251,622"/>
      </defs>
      <circle cx="283" cy="440" r="190" fill="url(#choc-spoon)" role="img" aria-label="Wooden spoon holding chocolate pieces in a splash of melted chocolate over a dotted halftone ring"/>
      <text class="flavour-arc"><textPath href="#choc-arc">CHOCOLATE DELUXE</textPath></text>
    </svg>
    <div class="brand-tab">
      <span class="brand-tab__name">ZEAL</span>
      <span class="brand-tab__tag">SUPPLEMENTS</span>
    </div>
    <div class="product-band"><span>PROTEIN</span><span>POWDER</span></div>
  </article>

</main>
</body>
</html>
```